lawncare business

Lawncare business. Definitely need company name( Pellbrookens) and slogan ( When your grass gets tall, give us a call) and of course contact info..I would like a unique logo that is lawncare related and alot of attention getting color on the card.

Industry/Entity Type

Business

Contact Information for Business Card

Owner: Dale Penwick Pellbrookens
(555) 614-2087 When your grass gets tall, give us a call.

Requirements
Must have
• Unique lawncare related logo......company name and slogan.....Contact info

```html
<!DOCTYPE html>
<html lang="en">
<head>
<meta charset="utf-8">
<title>Pellbrookens – Business Card</title>
<link rel="stylesheet" href="https://fonts.googleapis.com/css2?family=Fira+Sans:wght@600&family=Fira+Sans+Condensed:wght@600&family=Inter:wght@300&display=swap">
<style>
  :root {
    --paper: #ffffff;
    --brand-green: #22cc00;
    --deep-green: #1c8f1c;
    --lime: #a8f03c;
  }
  html, body {
    margin: 0;
    padding: 0;
    width: 1200px;
    height: 702px;
    overflow: hidden;
    background: var(--paper);
  }
  .card {
    position: relative;
    width: 1200px;
    height: 702px;
    background: var(--paper);
  }
  .brand {
    position: absolute;
    left: 52px;
    top: 58px;
    display: flex;
    align-items: center;
    gap: 18px;
  }
  .brand-square {
    width: 125px;
    height: 125px;
    background: var(--brand-green);
  }
  .brand-name {
    font-family: "Fira Sans", sans-serif;
    font-weight: 600;
    font-size: 66px;
    line-height: 1;
    letter-spacing: 0.5px;
    color: var(--brand-green);
    text-transform: uppercase;
  }
  .person {
    position: absolute;
    left: 0;
    width: 1234px;
    top: 300px;
    text-align: center;
  }
  .person-name {
    font-family: "Fira Sans Condensed", sans-serif;
    font-weight: 600;
    font-size: 56px;
    line-height: 1;
    color: var(--deep-green);
    margin: 0;
  }
  .person-role {
    font-family: "Inter", sans-serif;
    font-weight: 300;
    font-size: 38px;
    line-height: 1;
    color: var(--lime);
    margin: 12px 0 0;
    letter-spacing: 1px;
  }
  .slogan {
    position: absolute;
    left: 38px;
    top: 584px;
    font-family: "Inter", sans-serif;
    font-weight: 300;
    font-size: 29px;
    line-height: 39px;
    letter-spacing: -0.5px;
    color: var(--brand-green);
    margin: 0;
  }
  .phone {
    position: absolute;
    left: 655px;
    top: 580px;
    font-family: "Inter", sans-serif;
    font-weight: 300;
    font-size: 68px;
    line-height: 1;
    letter-spacing: -1px;
    color: var(--brand-green);
    margin: 0;
  }
</style>
</head>
<body>
  <main class="card">
    <header class="brand">
      <div class="brand-square"></div>
      <div class="brand-name">Pellbrookens</div>
    </header>

    <section class="person">
      <h1 class="person-name">Dale Penwick</h1>
      <p class="person-role">Owner</p>
    </section>

    <p class="slogan">When your grass gets tall,<br>give us a call !</p>

    <p class="phone">(555) 614-2087</p>
  </main>
</body>
</html>
```